Willowmere Counseling (Endure - Mend - Flourish) - Double Sided Business Card

I would like a 2-sided business card. Front: Matte Black or Navy with Logo & Tagline. Back: Name, Address, Phone Number, Email, & Website (maybe would like to include a small map pin-pointing location); Prefer front to be a gold/silver foil (iridescent); Back prefer white or light colored background with lettering that is easy to read and simple

Target Market(s)

Individuals & Couples (13 y.o. - ALL Adults); High end clientele

Industry/Entity Type

Licensed Professional Counselor (Mental Health)

Contact Information for Business Card

Name: Willowmere Counseling; Tagline: Endure - Mend - Flourish; Address: 3870 N. Garrick Ave., Suite 214, Fort Worth, TX 76132; Phone: (214) 555-0187; Website: www.WillowmereCounseling.example

Font styles to use
Serif

Requirements
Must have
• Logo on Front (Large) prefer gold/silver foil on a matte dark color (i.e. black, navy, etc.); Back of Card: All other relevant information

```html
<!DOCTYPE html>
<html lang="en">
<head>
<meta charset="utf-8">
<title>Willowmere Counseling – Business Card</title>
<link rel="stylesheet" href="https://fonts.googleapis.com/css2?family=Cinzel:wght@400;600;700&display=swap">
<style>
  :root {
    --page: #ffffff;
    --card-front: #222121;
    --card-back: #1e1c1d;
    --silver: #8a8b8d;
    --gold: #d4b451;
    --ink: #ffffff;
  }
  * { box-sizing: border-box; margin: 0; padding: 0; }
  html, body { width: 1038px; height: 1200px; overflow: hidden; background: var(--page); }
  body { position: relative; font-family: "Cinzel", "Times New Roman", serif; }

  .card {
    position: absolute; left: 51px; width: 936px; height: 534px;
    border-radius: 20px; overflow: hidden;
  }
  .card--front { top: 49px; background: var(--card-front); }
  .card--back { top: 614px; background: var(--card-back); }

  /* Front */
  .brand-mark { position: absolute; }
  .card--front .brand-mark { left: 394px; top: 136px; }
  .brand-name {
    position: absolute; left: 274px; width: 384px; top: 323px;
    text-align: center; color: var(--silver); font-weight: 400;
    font-size: 52px; line-height: 1; letter-spacing: 0.5px;
  }
  .brand-sub {
    position: absolute; left: 274px; width: 384px; top: 390px;
    display: flex; align-items: center; gap: 8px; color: var(--silver);
  }
  .brand-sub .rule { flex: 1; height: 3px; background: var(--silver); }
  .brand-sub span { font-size: 26px; letter-spacing: 6px; line-height: 1; }
  .brand-tagline {
    position: absolute; left: 274px; width: 384px; top: 424px;
    text-align: center; color: var(--silver); font-size: 18px; line-height: 1;
    letter-spacing: 0.3px;
  }

  /* Back */
  .card--back .brand-mark { left: 409px; top: 82px; }
  .identity {
    position: absolute; right: 487px; top: 308px; text-align: right; color: var(--ink);
  }
  .identity .name-1 { font-size: 40px; font-weight: 600; line-height: 1; display: block; }
  .identity .name-2 { font-size: 36px; font-weight: 600; line-height: 1; display: block; margin-top: 12px; }
  .identity .tagline { font-size: 17px; font-weight: 600; display: block; margin-top: 14px; letter-spacing: 0.3px; }

  .contact { position: absolute; left: 454px; top: 292px; list-style: none; color: var(--ink); }
  .contact li { display: flex; align-items: flex-start; margin-bottom: 20px; }
  .contact svg { width: 28px; height: 28px; flex: none; margin-right: 46px; margin-top: 2px; }
  .contact .text { font-size: 21px; font-weight: 600; line-height: 1.3; }
  .contact .web { font-size: 18px; padding-top: 4px; }
</style>
</head>
<body>

<section class="card card--front" aria-label="Card front">
  <svg class="brand-mark" width="142" height="142" viewBox="0 0 142 142" aria-hidden="true">
    <circle cx="71" cy="71" r="62" fill="none" stroke="var(--silver)" stroke-width="10"/>
  </svg>
  <h1 class="brand-name">WILLOWMERE</h1>
  <div class="brand-sub"><i class="rule"></i><span>COUNSELING</span><i class="rule"></i></div>
  <p class="brand-tagline">ENDURE - MEND - FLOURISH</p>
</section>

<section class="card card--back" aria-label="Card back">
  <svg class="brand-mark" width="132" height="132" viewBox="0 0 132 132" aria-hidden="true">
    <circle cx="66" cy="66" r="58" fill="none" stroke="var(--gold)" stroke-width="10"/>
  </svg>

  <div class="identity">
    <span class="name-1">Willowmere</span>
    <span class="name-2">Counseling</span>
    <span class="tagline">Endure - Mend - Flourish</span>
  </div>

  <ul class="contact">
    <li>
      <svg viewBox="0 0 28 28" aria-hidden="true" fill="none" stroke="var(--gold)" stroke-width="1.6">
        <path d="M14 26c-5-7-8-11-8-15a8 8 0 0 1 16 0c0 4-3 8-8 15z"/>
        <circle cx="14" cy="11" r="3"/>
      </svg>
      <span class="text">3870 N. Garrick Ave., Suite 214,<br>Fort Worth, TX 76132</span>
    </li>
    <li>
      <svg viewBox="0 0 28 28" aria-hidden="true" fill="none" stroke="var(--gold)" stroke-width="1.6" stroke-linejoin="round">
        <path d="M6 4l4 0 2 6-3 2c1 3 4 6 7 7l2-3 6 2v4c0 1-1 2-2 2C12 24 4 16 4 6c0-1 1-2 2-2z"/>
      </svg>
      <span class="text">(214) 555-0187</span>
    </li>
    <li>
      <svg viewBox="0 0 28 28" aria-hidden="true" fill="none" stroke="var(--gold)" stroke-width="1.6">
        <circle cx="14" cy="14" r="11"/>
        <ellipse cx="14" cy="14" rx="5" ry="11"/>
        <path d="M3 14h22M5 8h18M5 20h18"/>
      </svg>
      <span class="text web">www.WillowmereCounseling.example</span>
    </li>
  </ul>
</section>

</body>
</html>
```